Great looking banner designs for our website www.stoutwellcases.com

Our website is a key marketing platform and the banners need some work. We need 4-5 great looking banner designs.
StoutWell cases are the toughest around and have a unique accessory attachment system and range of accessories. We like to see banners that show our products, how they can be used and with key selling messages

Target Market(s)

Key markets are construction and outdoor workers, fishing and boating, cycling, camping and other adventure activities.

Industry/Entity Type

Marketing

Font styles to use
Other font styles liked:
• Homenaje

Requirements
Must have
• Ideally we'd like the banners to give customers a good idea of the capabilities of our products and the situations they can be used.

This is a dropbox link to a range of images and renders that can be used for the banners.
https://www.parcelnest.com/sh/k7p2qx9ma3tz118/Tq4vLmw8nE

We are also happy to look at increasing the banner size on the home page.

Banners should show the Zelvar case range + different accessories.
We have our new Stoutwell outdoor Bluetooth speaker arriving soon so need an appropriate banner
Banner size should be 1270 x 520

```html
<!DOCTYPE html>
<html lang="en">
<head>
<meta charset="utf-8">
<title>StoutWell Cases – Website Banners</title>
<link rel="stylesheet" href="https://fonts.googleapis.com/css2?family=Open+Sans:wght@400;600&display=swap">
<style>
  :root{
    --page:#ffffff;
    --ink:#0d0d0d;
    --rule:#e2e2e2;
    --text:#f2f2f2;
    --bar:#262626;
    --red:#d8232a;
    --sky:#7cc3dc;
    --blue:#2a86c8;
    --green:#5f9a4a;
    --tan:#c9a77a;
    --badge:#e2141c;
  }
  *{margin:0;padding:0;box-sizing:border-box}
  html,body{width:1200px;height:770px;overflow:hidden;background:var(--page)}
  body{position:relative;font-family:"Open Sans",Arial,sans-serif}
  .defs{position:absolute;width:0;height:0}

  .banner{position:absolute;width:528px;height:216px;background:var(--ink);overflow:hidden}
  .banner svg.art{position:absolute;inset:0;width:100%;height:100%;display:block}
  .col-left{left:44px}
  .col-right{left:630px}
  .row-1{top:23px}
  .row-2{top:277px}
  .row-3{top:531px}

  .claims{position:absolute;bottom:10px;list-style:none;color:var(--text);
    font-size:21px;line-height:33px;letter-spacing:.1px;text-transform:uppercase}
  .claims.at-left{left:0;padding-left:4px}
  .claims.at-right{right:0;text-align:right;padding-right:4px}
  .claims li{padding:0 6px;white-space:nowrap}
  .claims .proof{display:inline-block;min-width:210px;padding:0 4px;margin:0 -4px}
  .at-left .proof{background:linear-gradient(90deg,var(--bar) 0%,var(--bar) 70%,rgba(38,38,38,0) 100%)}
  .at-right .proof{background:linear-gradient(270deg,var(--bar) 0%,var(--bar) 70%,rgba(38,38,38,0) 100%)}
  .proof.red{color:var(--red)}
  .proof.sky{color:var(--sky)}
  .proof.blue{color:var(--blue)}
  .proof.green{color:var(--green)}
  .proof.tan{color:var(--tan)}

  .badge-new{position:absolute;left:312px;top:6px;width:78px;height:78px}
  .badge-new span{position:absolute;inset:0;display:flex;align-items:center;justify-content:center;
    color:#fff;font-size:22px;font-weight:600;letter-spacing:.5px}
</style>
</head>
<body>

<svg class="defs" aria-hidden="true">
  <defs>
    <linearGradient id="band" x1="0" y1="0" x2="0" y2="1">
      <stop offset="0" stop-color="#3a3a3a"/>
      <stop offset="1" stop-color="#111111"/>
    </linearGradient>
    <linearGradient id="sweep" x1="0" y1="0" x2="1" y2="0">
      <stop offset="0" stop-color="#050505"/>
      <stop offset=".55" stop-color="#1b1b1b"/>
      <stop offset="1" stop-color="#2e2e2e"/>
    </linearGradient>
    <linearGradient id="cases" x1="0" y1="0" x2="1" y2="0">
      <stop offset="0" stop-color="#d8558a"/>
      <stop offset=".25" stop-color="#d8558a"/>
      <stop offset=".3" stop-color="#9a9da4"/>
      <stop offset=".5" stop-color="#9a9da4"/>
      <stop offset=".55" stop-color="#2f3136"/>
      <stop offset=".72" stop-color="#2f3136"/>
      <stop offset=".77" stop-color="#e07a3a"/>
      <stop offset="1" stop-color="#e07a3a"/>
    </linearGradient>

    <!-- scene tones -->
    <linearGradient id="sea" x1="0" y1="0" x2="0" y2="1">
      <stop offset="0" stop-color="#4fc0cc"/><stop offset="1" stop-color="#16728c"/>
    </linearGradient>
    <radialGradient id="sea-spot" cx=".5" cy=".55" r=".45">
      <stop offset="0" stop-color="#e85a2a" stop-opacity=".85"/><stop offset="1" stop-color="#e85a2a" stop-opacity="0"/>
    </radialGradient>

    <linearGradient id="splash" x1="0" y1="0" x2="1" y2="1">
      <stop offset="0" stop-color="#8fbfd0"/><stop offset=".5" stop-color="#5e8ea6"/><stop offset="1" stop-color="#2b5a72"/>
    </linearGradient>
    <radialGradient id="splash-spot" cx=".55" cy=".45" r=".35">
      <stop offset="0" stop-color="#f06a2c" stop-opacity=".85"/><stop offset="1" stop-color="#f06a2c" stop-opacity="0"/>
    </radialGradient>

    <linearGradient id="palms" x1="0" y1="0" x2="0" y2="1">
      <stop offset="0" stop-color="#79b6e4"/><stop offset=".6" stop-color="#a6cce4"/><stop offset="1" stop-color="#35603c"/>
    </linearGradient>
    <radialGradient id="palms-spot" cx=".6" cy=".35" r=".4">
      <stop offset="0" stop-color="#e87a3a" stop-opacity=".7"/><stop offset="1" stop-color="#e87a3a" stop-opacity="0"/>
    </radialGradient>

    <linearGradient id="map" x1="0" y1="0" x2="1" y2="1">
      <stop offset="0" stop-color="#c6cbb6"/><stop offset=".55" stop-color="#8c977d"/><stop offset="1" stop-color="#3f4a37"/>
    </linearGradient>
    <radialGradient id="map-spot" cx=".5" cy=".6" r=".35">
      <stop offset="0" stop-color="#1e1e1e" stop-opacity=".7"/><stop offset="1" stop-color="#1e1e1e" stop-opacity="0"/>
    </radialGradient>

    <linearGradient id="beach" x1="0" y1="0" x2="0" y2="1">
      <stop offset="0" stop-color="#86c0de"/><stop offset=".5" stop-color="#5d9fc4"/><stop offset="1" stop-color="#d2b69a"/>
    </linearGradient>
    <radialGradient id="beach-spot" cx=".5" cy=".65" r=".4">
      <stop offset="0" stop-color="#e47aa2" stop-opacity=".75"/><stop offset="1" stop-color="#e47aa2" stop-opacity="0"/>
    </radialGradient>

    <linearGradient id="table" x1="0" y1="0" x2="0" y2="1">
      <stop offset="0" stop-color="#a4aab0"/><stop offset="1" stop-color="#3a3e43"/>
    </linearGradient>
    <radialGradient id="table-spot" cx=".4" cy=".6" r=".45">
      <stop offset="0" stop-color="#161a1e" stop-opacity=".8"/><stop offset=".7" stop-color="#3aa8d8" stop-opacity=".25"/><stop offset="1" stop-color="#3aa8d8" stop-opacity="0"/>
    </radialGradient>

    <clipPath id="below">
      <path d="M0 66 C140 42 300 122 528 98 V216 H0Z"/>
    </clipPath>
  </defs>
</svg>

<!-- Row 1 -->
<section class="banner col-left row-1">
  <svg class="art" viewBox="0 0 528 216" preserveAspectRatio="none">
    <path d="M0 0 H528 V98 C300 122 140 42 0 66Z" fill="url(#band)"/>
    <path d="M150 0 C260 20 360 60 528 56 V0Z" fill="url(#sweep)"/>
    <g role="img" aria-label="Man in an orange life jacket in clear sea water holding a cased phone" clip-path="url(#below)">
      <rect x="234" y="0" width="294" height="216" fill="url(#sea)"/>
      <rect x="234" y="0" width="294" height="216" fill="url(#sea-spot)"/>
    </g>
    <path d="M0 62 C140 38 300 118 528 94" fill="none" stroke="var(--rule)" stroke-width="3"/>
    <g role="img" aria-label="Row of four coloured phone cases"><rect x="410" y="6" width="96" height="36" rx="3" fill="url(#cases)"/></g>
  </svg>
  <ul class="claims at-left">
    <li>Durable.</li>
    <li>Reliable.</li>
    <li><span class="proof red">Shockproof.</span></li>
  </ul>
</section>

<section class="banner col-right row-1">
  <svg class="art" viewBox="0 0 528 216" preserveAspectRatio="none">
    <path d="M0 0 H528 V98 C300 122 140 42 0 66Z" fill="url(#band)"/>
    <path d="M150 0 C260 20 360 60 528 56 V0Z" fill="url(#sweep)"/>
    <g role="img" aria-label="Orange waterproof phone pouch splashing into water" clip-path="url(#below)">
      <rect x="222" y="0" width="306" height="216" fill="url(#splash)"/>
      <rect x="222" y="0" width="306" height="216" fill="url(#splash-spot)"/>
    </g>
    <path d="M0 62 C140 38 300 118 528 94" fill="none" stroke="var(--rule)" stroke-width="3"/>
    <g role="img" aria-label="Row of four coloured phone cases"><rect x="28" y="6" width="96" height="36" rx="3" fill="url(#cases)"/></g>
  </svg>
  <ul class="claims at-left">
    <li>Durable.</li>
    <li>Stylish.</li>
    <li><span class="proof sky">Oops proof.</span></li>
  </ul>
</section>

<!-- Row 2 -->
<section class="banner col-left row-2">
  <svg class="art" viewBox="0 0 528 216" preserveAspectRatio="none">
    <path d="M0 0 H528 V98 C300 122 140 42 0 66Z" fill="url(#band)"/>
    <path d="M150 0 C260 20 360 60 528 56 V0Z" fill="url(#sweep)"/>
    <g role="img" aria-label="Hand opening a bottle with an orange case bottle-opener accessory under palm trees" clip-path="url(#below)">
      <rect x="0" y="0" width="312" height="216" fill="url(#palms)"/>
      <rect x="0" y="0" width="312" height="216" fill="url(#palms-spot)"/>
    </g>
    <path d="M0 62 C140 38 300 118 528 94" fill="none" stroke="var(--rule)" stroke-width="3"/>
    <g role="img" aria-label="Row of four coloured phone cases"><rect x="28" y="6" width="96" height="36" rx="3" fill="url(#cases)"/></g>
  </svg>
  <ul class="claims at-right">
    <li>Durable.</li>
    <li>Attractive.</li>
    <li><span class="proof blue">Boredom proof.</span></li>
  </ul>
</section>

<section class="banner col-right row-2">
  <svg class="art" viewBox="0 0 528 216" preserveAspectRatio="none">
    <path d="M0 0 H528 V98 C300 122 140 42 0 66Z" fill="url(#band)"/>
    <path d="M150 0 C260 20 360 60 528 56 V0Z" fill="url(#sweep)"/>
    <g role="img" aria-label="Hand holding a black cased phone with compass app over a trail map outdoors" clip-path="url(#below)">
      <rect x="0" y="0" width="303" height="216" fill="url(#map)"/>
      <rect x="0" y="0" width="303" height="216" fill="url(#map-spot)"/>
    </g>
    <path d="M0 62 C140 38 300 118 528 94" fill="none" stroke="var(--rule)" stroke-width="3"/>
    <g role="img" aria-label="Row of four coloured phone cases"><rect x="28" y="6" width="96" height="36" rx="3" fill="url(#cases)"/></g>
  </svg>
  <ul class="claims at-right">
    <li>Durable.</li>
    <li>Invaluable.</li>
    <li><span class="proof green">Outdoors proof.</span></li>
  </ul>
</section>

<!-- Row 3 -->
<section class="banner col-left row-3">
  <svg class="art" viewBox="0 0 528 216" preserveAspectRatio="none">
    <path d="M0 0 H528 V98 C300 122 140 42 0 66Z" fill="url(#band)"/>
    <path d="M150 0 C260 20 360 60 528 56 V0Z" fill="url(#sweep)"/>
    <g role="img" aria-label="Two girls on a beach laughing at a phone in a pink case" clip-path="url(#below)">
      <rect x="217" y="0" width="311" height="216" fill="url(#beach)"/>
      <rect x="217" y="0" width="311" height="216" fill="url(#beach-spot)"/>
    </g>
    <path d="M0 62 C140 38 300 118 528 94" fill="none" stroke="var(--rule)" stroke-width="3"/>
    <g role="img" aria-label="Row of four coloured phone cases"><rect x="28" y="6" width="96" height="36" rx="3" fill="url(#cases)"/></g>
  </svg>
  <ul class="claims at-left">
    <li>Durable.</li>
    <li>Easy to use.</li>
    <li><span class="proof tan">Giggle proof.</span></li>
  </ul>
</section>

<section class="banner col-right row-3">
  <svg class="art" viewBox="0 0 528 216" preserveAspectRatio="none">
    <path d="M0 0 H528 V98 C300 122 140 42 0 66Z" fill="url(#band)"/>
    <path d="M150 0 C260 20 360 60 528 56 V0Z" fill="url(#sweep)"/>
    <g role="img" aria-label="Outdoor Bluetooth speaker with blue trim beside a rugged cased phone on a table" clip-path="url(#below)">
      <rect x="0" y="0" width="305" height="216" fill="url(#table)"/>
      <rect x="0" y="0" width="305" height="216" fill="url(#table-spot)"/>
    </g>
    <path d="M0 62 C140 38 300 118 528 94" fill="none" stroke="var(--rule)" stroke-width="3"/>
    <g role="img" aria-label="Row of four coloured phone cases"><rect x="28" y="6" width="96" height="36" rx="3" fill="url(#cases)"/></g>
  </svg>
  <div class="badge-new">
    <svg viewBox="0 0 100 100" width="78" height="78" aria-hidden="true">
      <polygon fill="var(--badge)" points="50,0 57,14 71,5 73,21 89,17 84,32 100,36 89,48 100,60 85,65 91,80 75,79 74,95 60,87 50,100 40,87 26,95 25,79 9,80 15,65 0,60 11,48 0,36 16,32 11,17 27,21 29,5 43,14"/>
    </svg>
    <span>NEW</span>
  </div>
  <ul class="claims at-right">
    <li>Durable.</li>
    <li>Portable.</li>
    <li><span class="proof red">Wire proof.</span></li>
  </ul>
</section>

</body>
</html>
```